Tag design needed for wall art products

We need to design a tag for wall art products, which are Canvas, wood art, and rolling canvas.

The Tag need to be classical which means not too colorful, all information in the file (1pic) need to be included such as brand name, company website.

The side of tag need to be same as Quvia 4 or Quvia 5 with a hole on the top.
Updates

More designs are required!

Target Market(s)

US Market

Industry/Entity Type

Home And Garden

Requirements
Must have
• ART.DECORATION
• RUDFERN&BLISARTS
• 1978
• WWW.BLISFRAMEX.COM
• HONGKONG AUSTRALIA CHINA

```html
<!DOCTYPE html>
<html lang="en">
<head>
<meta charset="utf-8">
<title>Rudfern &amp; Blisarts — Hang Tags</title>
<link rel="stylesheet" href="https://fonts.googleapis.com/css2?family=Playfair+Display:wght@400&family=Source+Sans+3:wght@300;400&display=swap">
<style>
  :root {
    --page: #d9d9d9;
    --gold: #c79a4e;
    --gold-light: #e6c98a;
    --gold-deep: #8f6226;
    --noir: #161616;
    --ivory: #f5f3ef;
    --serif: "Playfair Display", Georgia, serif;
    --sans: "Source Sans 3", "Helvetica Neue", Arial, sans-serif;
  }
  * { box-sizing: border-box; margin: 0; padding: 0; }
  html, body { width: 1200px; height: 900px; overflow: hidden; }
  body { background: var(--page); position: relative; }

  .tag {
    position: absolute;
    top: 41px;
    width: 372px;
    height: 818px;
    text-align: center;
  }
  .tag--noir { left: 157px; background: var(--noir); }
  .tag--ivory { left: 647px; background: var(--ivory); }

  .tag__frame {
    position: absolute;
    inset: 6px;
    border: 4px dotted var(--gold);
    opacity: 0.85;
  }

  .tag__hole {
    position: absolute;
    left: 50%;
    top: 53px;
    width: 60px;
    height: 60px;
    margin-left: -30px;
  }

  .tag__line {
    position: absolute;
    left: 0;
    right: 0;
    color: var(--gold);
  }

  .tag__category {
    top: 146px;
    font-family: var(--sans);
    font-weight: 300;
    font-size: 20px;
    letter-spacing: 4px;
  }

  .tag__brand {
    top: 270px;
    font-family: var(--serif);
    font-weight: 400;
    font-size: 40px;
    line-height: 44px;
    letter-spacing: 0.5px;
  }

  .tag__divider {
    position: absolute;
    top: 386px;
    left: 101px;
    width: 170px;
    height: 5px;
  }

  .tag__year {
    top: 410px;
    font-family: var(--serif);
    font-size: 32px;
  }

  .tag__url {
    top: 648px;
    font-family: var(--sans);
    font-weight: 400;
    font-size: 24px;
    letter-spacing: 1px;
  }

  .tag__regions {
    top: 760px;
    font-family: var(--sans);
    font-weight: 300;
    font-size: 15px;
    letter-spacing: 2.6px;
  }

  .ornament {
    position: absolute;
    left: 50%;
    border-radius: 4px;
    background: radial-gradient(ellipse at center, var(--gold-light) 0%, var(--gold) 45%, var(--gold-deep) 100%);
    opacity: 0.9;
  }
  .ornament--top { top: 193px; width: 264px; height: 42px; margin-left: -132px; }
  .ornament--crest {
    top: 472px; width: 203px; height: 143px; margin-left: -101px;
    border-radius: 40% 40% 50% 50% / 30% 30% 70% 70%;
  }
  .ornament--bottom { top: 694px; width: 299px; height: 62px; margin-left: -150px; }
</style>
</head>
<body>

  <article class="tag tag--noir">
    <div class="tag__frame"></div>
    <svg class="tag__hole" viewBox="0 0 60 60" aria-hidden="true">
      <circle cx="30" cy="30" r="29" fill="#c79a4e"/>
      <circle cx="30" cy="30" r="11" fill="#d9d9d9"/>
    </svg>
    <p class="tag__line tag__category">ART·DECORATION</p>
    <div class="ornament ornament--top" role="img" aria-label="Gold foil scrollwork border"></div>
    <h1 class="tag__line tag__brand">RUDFERN<br>&amp;BLISARTS</h1>
    <svg class="tag__divider" viewBox="0 0 170 5" aria-hidden="true">
      <line x1="0" y1="2.5" x2="170" y2="2.5" stroke="#c79a4e" stroke-width="1"/>
      <rect x="60" y="1" width="50" height="3" fill="#c79a4e"/>
    </svg>
    <p class="tag__line tag__year">1978</p>
    <div class="ornament ornament--crest" role="img" aria-label="Gold foil ornamental crest"></div>
    <p class="tag__line tag__url">WWW.BLISFRAMEX.COM</p>
    <div class="ornament ornament--bottom" role="img" aria-label="Gold foil floral frieze"></div>
    <p class="tag__line tag__regions">HONGKONG · AUSTRALIA · CHINA</p>
  </article>

  <article class="tag tag--ivory">
    <div class="tag__frame"></div>
    <svg class="tag__hole" viewBox="0 0 60 60" aria-hidden="true">
      <circle cx="30" cy="30" r="29" fill="#c79a4e"/>
      <circle cx="30" cy="30" r="11" fill="#d9d9d9"/>
    </svg>
    <p class="tag__line tag__category">ART·DECORATION</p>
    <div class="ornament ornament--top" role="img" aria-label="Gold foil scrollwork border"></div>
    <h1 class="tag__line tag__brand">RUDFERN<br>&amp;BLISARTS</h1>
    <svg class="tag__divider" viewBox="0 0 170 5" aria-hidden="true">
      <line x1="0" y1="2.5" x2="170" y2="2.5" stroke="#c79a4e" stroke-width="1"/>
      <rect x="60" y="1" width="50" height="3" fill="#c79a4e"/>
    </svg>
    <p class="tag__line tag__year">1978</p>
    <div class="ornament ornament--crest" role="img" aria-label="Gold foil ornamental crest"></div>
    <p class="tag__line tag__url">WWW.BLISFRAMEX.COM</p>
    <div class="ornament ornament--bottom" role="img" aria-label="Gold foil floral frieze"></div>
    <p class="tag__line tag__regions">HONGKONG · AUSTRALIA · CHINA</p>
  </article>

</body>
</html>
```